BrightLane Real Estate Sign

We are in the process of rebranding our business and need a new For Sale \ Sold sign.
We're a prestige real estate agency and therefore require a really stylish sign.
I've uploaded the following files
1. The new company logo
2. "sample sign.jpg" which shows the type of sign we would like. It is a metal sign with a top panel and bottom panel.
3. Our previous sign "previous sign.jpg" if you're interested in seeing it.
The sign must be black with white text.
Our thoughts are that the top panel (refer to sample sign) would contain the text "For Sale" or "Sold". These would be two separate panels which are interchangeable and could be screwed in place.
The bottom panel would not contain any photos like the sample. However, it may contain our logo and my contact details etc.
The sign is 900mm wide x 1200mm high.
My details are:
Name: Desmond Harlow
Web: www.blrealestate.com.au
Email: sales@blrealestate.com.au
Phone: 0491 836 205

```html
<!DOCTYPE html>
<html lang="en">
<head>
<meta charset="utf-8">
<title>BrightLane Real Estate – Sale Sign</title>
<link rel="stylesheet" href="https://fonts.googleapis.com/css2?family=Roboto:wght@300;400;700&display=swap">
<style>
  :root {
    --page-bg: #dcecf6;
    --panel-white: #ffffff;
    --sale-red: #e3232b;
    --sign-black: #050505;
    --metal-dark: #121212;
    --metal-mid: #2e2e2e;
    --text-white: #ffffff;
    --rule-grey: #8a8a8a;
  }
  * { box-sizing: border-box; margin: 0; padding: 0; }
  html, body {
    width: 1200px; height: 1000px; overflow: hidden;
    background: var(--page-bg);
    font-family: "Roboto", "Helvetica Neue", Arial, sans-serif;
  }
  .sign {
    position: absolute; left: 260px; top: 43px;
    width: 680px; height: 914px;
    background: var(--sign-black);
    box-shadow: 0 4px 12px rgba(0,0,0,0.25);
    overflow: hidden;
  }
  .sign__header {
    height: 227px; background: var(--panel-white);
    display: flex; align-items: center; justify-content: center;
  }
  .sign__headline {
    font-weight: 300; font-size: 228px; line-height: 1;
    letter-spacing: 18px; color: var(--sale-red);
    margin-left: 18px;
  }
  .sign__contact {
    position: relative; height: 438px; overflow: hidden;
  }
  .sign__texture {
    position: absolute; inset: 0;
    background: radial-gradient(ellipse at 50% 45%, var(--metal-mid) 0%, var(--metal-dark) 70%, #0a0a0a 100%);
  }
  .contact__body {
    position: relative; padding: 128px 0 0 48px; color: var(--text-white);
  }
  .contact__name {
    font-weight: 400; font-size: 76px; line-height: 1; letter-spacing: -1px;
    white-space: nowrap;
    margin-bottom: 16px;
  }
  .contact__list { list-style: none; }
  .contact__item {
    display: flex; align-items: center; gap: 18px;
    font-size: 36px; font-weight: 400; line-height: 49px;
    white-space: nowrap;
  }
  .contact__icon { width: 36px; height: 30px; flex: none; }
  .sign__brand {
    height: 249px; display: flex; align-items: center; justify-content: center; gap: 28px;
    color: var(--text-white);
  }
  .brand__mark { width: 84px; height: 84px; background: var(--text-white); }
  .brand__rule { width: 2px; height: 170px; background: var(--rule-grey); }
  .brand__text { display: flex; flex-direction: column; align-items: center; }
  .brand__name {
    font-weight: 700; font-size: 68px; line-height: 1; letter-spacing: -1px;
  }
  .brand__sub {
    font-weight: 400; font-size: 28px; line-height: 1; letter-spacing: 7px;
    margin-top: 8px;
  }
</style>
</head>
<body>
  <main class="sign">
    <header class="sign__header">
      <h1 class="sign__headline">SALE</h1>
    </header>

    <section class="sign__contact">
      <div class="sign__texture" role="img" aria-label="Dark perforated metal texture background"></div>
      <div class="contact__body">
        <h2 class="contact__name">Desmond Harlow</h2>
        <ul class="contact__list">
          <li class="contact__item">
            <svg class="contact__icon" viewBox="0 0 36 30" fill="none" stroke="#fff" stroke-width="3">
              <rect x="2" y="2" width="32" height="20"/><line x1="18" y1="22" x2="18" y2="27"/><line x1="9" y1="28" x2="27" y2="28"/>
            </svg>
            www.blrealestate.com.au
          </li>
          <li class="contact__item">
            <svg class="contact__icon" viewBox="0 0 36 30" fill="none" stroke="#fff" stroke-width="3" stroke-linejoin="round">
              <path d="M2 12 L18 2 L34 12 V28 H2 Z"/><path d="M2 12 L18 22 L34 12"/>
            </svg>
            sales@blrealestate.com.au
          </li>
          <li class="contact__item">
            <svg class="contact__icon" viewBox="0 0 36 30" fill="#fff">
              <path d="M2 10 Q18 -2 34 10 L30 14 L25 11 L25 8 Q18 5 11 8 L11 11 L6 14 Z"/>
              <path d="M10 14 H26 L32 28 H4 Z"/>
            </svg>
            0491 836 205
          </li>
        </ul>
      </div>
    </section>

    <footer class="sign__brand">
      <span class="brand__mark" aria-hidden="true"></span>
      <span class="brand__rule" aria-hidden="true"></span>
      <span class="brand__text">
        <span class="brand__name">BrightLane</span>
        <span class="brand__sub">REAL ESTATE</span>
      </span>
    </footer>
  </main>
</body>
</html>
```